Business card design needed for Renewable utilities company based in New Zealand.

We supply and install solar panels and all components along with it for a fully customisable PV system that helps customer save money on their energy bills right away and also save the planet!

I have attached logo & website design files to give you a better insight.

Industry/Entity Type

Business

```html
<!DOCTYPE html>
<html lang="en">
<head>
<meta charset="utf-8">
<title>Sunward Grid – Business Card</title>
<link href="https://fonts.googleapis.com/css2?family=Quicksand:wght@500&family=Open+Sans:wght@400;600&display=swap" rel="stylesheet">
<style>
  :root {
    --backdrop: #e9e6e1;
    --card-blue: #1f4f91;
    --card-blue-deep: #173e78;
    --card-blue-glow: #2c66ad;
    --map-tone: rgba(120, 165, 220, 0.18);
    --text-white: #ffffff;
    --accent-sky: #5db3e6;
    --rule-sky: #4f9fd6;
    --icon-fill: #4a9bd8;
    --faint-mark: rgba(255, 255, 255, 0.07);
  }
  * { margin: 0; padding: 0; box-sizing: border-box; }
  html, body {
    width: 1200px; height: 1023px; overflow: hidden;
    background: var(--backdrop);
  }
  .canvas { position: relative; width: 1200px; height: 1023px; }

  .card {
    position: absolute;
    width: 700px; height: 400px;
    border-radius: 4px;
    background: radial-gradient(ellipse at 55% 40%, var(--card-blue-glow) 0%, var(--card-blue) 45%, var(--card-blue-deep) 100%);
    color: var(--text-white);
    overflow: hidden;
    box-shadow: 0 6px 18px rgba(0, 0, 0, 0.18);
  }
  .card--front { left: 120px; top: 70px; }
  .card--back { left: 380px; top: 553px; }

  /* Front */
  .world-map {
    position: absolute; left: 90px; top: 60px; width: 520px; height: 250px;
    border-radius: 40% 45% 38% 42%;
    background: radial-gradient(ellipse at center, var(--map-tone) 0%, rgba(120, 165, 220, 0.08) 60%, transparent 100%);
  }
  .front-brand {
    position: absolute; left: 0; right: 0; top: 120px;
    display: flex; flex-direction: column; align-items: center; gap: 22px;
  }
  .brand-dot {
    width: 96px; height: 96px; border-radius: 50%;
    background: var(--text-white);
  }
  .brand-name {
    font-family: "Quicksand", sans-serif; font-weight: 500;
    color: var(--text-white); letter-spacing: 1px;
  }
  .front-brand .brand-name { font-size: 46px; }
  .front-website {
    position: absolute; left: 0; right: 0; bottom: 34px; text-align: center;
    font-family: "Open Sans", sans-serif; font-size: 19px; letter-spacing: 0.5px;
  }

  /* Back */
  .back-brand {
    position: absolute; left: 44px; top: 46px;
    display: flex; flex-direction: column; align-items: center; gap: 14px;
  }
  .back-brand .brand-dot { width: 86px; height: 86px; }
  .back-brand .brand-name { font-size: 38px; }
  .holder {
    position: absolute; right: 40px; top: 178px; text-align: right;
    font-family: "Open Sans", sans-serif;
  }
  .holder-name { font-size: 25px; font-weight: 600; color: var(--accent-sky); letter-spacing: 0.3px; }
  .holder-role { font-size: 15px; margin-top: 2px; }
  .divider {
    position: absolute; left: 48px; top: 242px; width: 470px; height: 2px;
    background: var(--rule-sky);
  }
  .contact-list {
    position: absolute; left: 54px; top: 278px; list-style: none;
    font-family: "Open Sans", sans-serif; font-size: 15.5px; line-height: 21px;
  }
  .contact-list li { display: flex; align-items: center; gap: 9px; }
  .contact-icon { width: 16px; height: 16px; flex: none; }
  .faint-mark {
    position: absolute; right: 70px; bottom: 18px; width: 150px; height: 150px;
    border-radius: 50%; background: var(--faint-mark);
  }
</style>
</head>
<body>
<main class="canvas">

  <section class="card card--front" aria-label="Card front">
    <div class="world-map" role="img" aria-label="Dotted world map in faint blue"></div>
    <div class="front-brand">
      <span class="brand-dot"></span>
      <span class="brand-name">Sunward Grid</span>
    </div>
    <p class="front-website">www.yourwebsite.co.nz</p>
  </section>

  <section class="card card--back" aria-label="Card back">
    <div class="back-brand">
      <span class="brand-dot"></span>
      <span class="brand-name">Sunward Grid</span>
    </div>
    <div class="holder">
      <p class="holder-name">John Doe Smith</p>
      <p class="holder-role">General Manager</p>
    </div>
    <div class="divider"></div>
    <ul class="contact-list">
      <li>
        <svg class="contact-icon" viewBox="0 0 16 16"><circle cx="8" cy="8" r="8" fill="var(--icon-fill)"/><rect x="5.5" y="3.5" width="5" height="9" rx="1" fill="none" stroke="#fff" stroke-width="1.2"/></svg>
        (03) 234 5678
      </li>
      <li>
        <svg class="contact-icon" viewBox="0 0 16 16"><circle cx="8" cy="8" r="8" fill="var(--icon-fill)"/><path d="M4 6.5 Q8 3.5 12 6.5 V7.5 H10 V6.8 H6 V7.5 H4 Z M5 8.5 H11 V11.5 H5 Z" fill="#fff"/></svg>
        0507 123 456
      </li>
      <li>
        <svg class="contact-icon" viewBox="0 0 16 16"><circle cx="8" cy="8" r="8" fill="var(--icon-fill)"/><rect x="4" y="5" width="8" height="6" fill="#fff"/><path d="M4 5 L8 8.5 L12 5" fill="none" stroke="var(--icon-fill)" stroke-width="1"/></svg>
        support@yourwebsite.co.nz
      </li>
      <li>
        <svg class="contact-icon" viewBox="0 0 16 16"><circle cx="8" cy="8" r="8" fill="var(--icon-fill)"/><circle cx="8" cy="8" r="4" fill="none" stroke="#fff" stroke-width="1"/><ellipse cx="8" cy="8" rx="1.8" ry="4" fill="none" stroke="#fff" stroke-width="0.9"/><line x1="4" y1="8" x2="12" y2="8" stroke="#fff" stroke-width="0.9"/></svg>
        www.yourwebsite.co.nz
      </li>
      <li>
        <svg class="contact-icon" viewBox="0 0 16 16"><circle cx="8" cy="8" r="8" fill="var(--icon-fill)"/><path d="M8 12.5 C5.5 9.5 5 8.3 5 7 A3 3 0 0 1 11 7 C11 8.3 10.5 9.5 8 12.5 Z" fill="#fff"/><circle cx="8" cy="7" r="1.1" fill="var(--icon-fill)"/></svg>
        #101 Office Address, Single Line, NZ
      </li>
    </ul>
    <span class="faint-mark"></span>
  </section>

</main>
</body>
</html>
```